New UI for electricity data tool

We are looking for a new UI for the website http://vantorgrid.net. Reassessing the structure of the website is as important as specific design choices. We have created a uniquely comprehensive set of global electricity generation data and now we are looking for creative solutions for how to make this data accessible. Researching and referencing other similar projects may be a good idea.

Goals:
• The website should clearly communicate the most important general conclusions that can be drawn from the data, including:
◦ The world as a whole is not moving away from fossil fuels for electricity generation
◦ There are substantial differences between regions
▪ Some regions have basically solved the problem – they already generate almost all of their electricity from non-fossil sources
▪ Some regions have greatly improved in terms of decarbonizing their electricity generation.
▪ Some regions have greatly deteriorated, in other words they are using a much higher share of fossil fuels to generate their electricity.
◦ There are substantial differences between energy sources. Regions that have successfully decarbonized their electricity generation have usually done so using hydro and/or nuclear. Other low-carbon energy sources have grown quickly in relative terms in the last few years but are so far contributing little in absolute numbers.
• The website should serve as inspiration for energy policy debates. The goal is to study the impact of existing policies around the world. Energy policy here refers to particular combinations of energy sources – ie how much have the countries invested in each type of electricity generation. The tool should help answer questions such as:
◦ Which countries have done the most in terms of decarbonizing their electricity generation?
◦ Which types of energy polices have lead to the fastest decarbonization processes around the world?
◦ If country A changed its energy policy to be more like country B, what would the likely impact be?

Challenges:
• There is a lot of data – it can be overwhelming to the user. It’s crucial to make the site easy to navigate. The main page should highlight the most important data, and it should also be straightforward to find more detailed data.
• Data availability varies from region to region. The current interface addresses this with the default option “Exclude regions with limited data”. We expect a better approach to dealing with this issue. For some regions and years energy sources are grouped together as for example “other renewables” whereas in other cases more detailed data is available.
• Credibility is crucial. Our data is based on a combination of data from KQ and the Tessary Trust. It must be very clear throughout the site where each data set comes from.

Details:
• The current chart color schemes is loosely based on the carbon emissions from each energy source. This should not necessarily be so. The goal is to on the one hand communicate clearly the amounts of fossil vs non-fossil energy that are generated by each region. At the same time we also want to make it easy to view specific energy sources.

Inspirational websites:
• https://www.grafmelo.org/
• https://trendquarrily.org/

Let's simplify. The main metric to focus on is Brisavolt Index and the extent to which the world and each country has achieved it (eg Iceland 100%, France 88% and so on). I'm considering changing the name of the site to BrisavoltIndex.org. We can use maps, charts and perhaps other tools to communicate this main message. What's the best way of doing this?

```html
<!DOCTYPE html>
<html lang="en">
<head>
<meta charset="utf-8">
<title>Clean Electricity</title>
<link href="https://fonts.googleapis.com/css2?family=Lato:ital,wght@0,400;0,700;0,900;1,400;1,700&display=swap" rel="stylesheet">
<style>
:root{
  --teal-deep:#086a68;
  --teal:#0f7f7b;
  --teal-soft:#2d8f88;
  --cyan:#14c2c2;
  --sky:#3ad8f0;
  --navy:#1b2d48;
  --ink:#222;
  --muted:#555;
  --panel:#e3e3e3;
  --plot:#ececec;
  --hydro:#5e93f5;
  --nuclear:#3ad8f0;
  --renew:#6cbf3a;
  --pink:#f07a84;
}
*{box-sizing:border-box;margin:0;padding:0}
html,body{width:1200px;height:3154px;overflow:hidden;background:#fff}
body{font-family:'Lato',sans-serif;color:var(--ink);position:relative}
.abs{position:absolute}

/* header */
.site-header{position:absolute;left:0;top:0;width:1200px;height:75px;background:var(--teal-deep);color:#fff;text-align:center}
.site-title{font-size:22px;font-weight:700;padding-top:13px;letter-spacing:.2px}
.site-tagline{font-size:12px;margin-top:5px}

/* nav */
.main-nav{position:absolute;left:149px;top:98px;display:flex;gap:0;font-size:12px;text-transform:uppercase;color:#222}
.main-nav a{color:inherit;text-decoration:none;margin-right:34px}
.main-nav a.active{color:var(--teal)}
.search{position:absolute;left:825px;top:90px;width:225px;height:30px;border:2px solid var(--teal-deep);border-radius:16px}
.search span{position:absolute;left:13px;top:8px;font-size:8px;color:#888}
.search b{position:absolute;right:4px;top:4px;width:70px;height:18px;border-radius:9px;background:var(--teal-deep);color:#fff;font-size:8px;text-align:center;line-height:18px;font-weight:700}
.rule{position:absolute;left:150px;width:900px;height:2px;background:var(--teal)}

.section-title{position:absolute;left:0;width:1200px;text-align:center;font-size:19px;color:#333}

/* leading regions */
.region-pill{position:absolute;left:150px;width:152px;height:23px;border-radius:12px;background:var(--teal-deep);color:#fff;font-size:12px;font-weight:700;text-align:center;line-height:23px}
.region-pill.hover{background:var(--cyan)}
.progress-label{position:absolute;left:322px;width:100px;text-align:center;color:var(--teal);font-style:italic}
.progress-label b{display:block;font-size:11px;font-weight:400}
.progress-label small{display:block;font-size:8px;margin-top:2px}
.progress{position:absolute;left:440px;width:610px;height:23px;border:1.5px solid var(--teal);border-radius:12px;overflow:hidden}
.progress-fill{height:100%;border-radius:12px;background:linear-gradient(90deg,#1d355a 0,#1d4a6a 25%,#118a8a 45%,#13b59c 100%);color:#fff;font-size:9px;line-height:20px;padding-left:25px;white-space:nowrap;font-weight:700;word-spacing:2px}
.progress-fill i{font-style:normal;margin-right:12px}
.region-text{position:absolute;left:150px;width:900px;font-size:15px;line-height:24px;color:#222}
.region-text em{font-style:normal;color:var(--teal)}
.read-more{position:absolute;left:968px;width:82px;height:14px;border-radius:7px;background:var(--teal-deep);color:#fff;font-size:6.5px;font-weight:700;text-align:center;line-height:14px}

/* data section header */
.data-label{position:absolute;left:150px;width:152px;height:29px;background:linear-gradient(90deg,#1d7f79,#3a9a92);color:#fff;font-size:22px;text-align:center;line-height:29px}
.ctl{position:absolute;height:28px;border-radius:14px;border:2px solid var(--teal-deep);color:var(--teal-deep);font-size:10px;line-height:24px;padding-left:14px}
.ctl::after{content:"";position:absolute;right:14px;top:8px;border-left:5px solid transparent;border-right:5px solid transparent;border-top:8px solid var(--teal-deep)}
.btn{position:absolute;height:28px;border-radius:14px;background:var(--teal-deep);color:#fff;font-size:10px;font-weight:700;text-align:center;line-height:28px}
.summary{position:absolute;left:150px;font-size:13px;color:#222}
.summary em{font-style:normal;color:var(--teal)}

/* info panel */
.info{position:absolute;left:825px;width:225px;height:300px;background:var(--panel);font-size:13px;line-height:19.5px;color:#333;padding:12px 0 0 0}
.info::before{content:"";position:absolute;left:-25px;top:2px;width:25px;height:28px;background:var(--panel);clip-path:polygon(0 20%,100% 0,100% 100%)}
.info p{padding-left:40px}
.info p.head{padding-left:27px;font-weight:700;position:relative}
.info p.key{padding-left:27px;position:relative}
.info p.key::before,.info p.head.sq::before{content:"";position:absolute;left:15px;top:6px;width:7px;height:7px;background:var(--c)}
.info p.gap{margin-top:10px}
.info .src{position:absolute;left:15px;right:15px;bottom:10px;display:flex;justify-content:space-between}
.info .src em{font-style:normal;color:var(--teal);font-weight:700}
.date{position:absolute;font-size:13px;color:#333}
.date em{font-style:normal;color:var(--teal);font-weight:700}

/* power sources */
.source-pill{position:absolute;top:1670px;width:104px;height:45px;border-radius:23px;color:#fff;font-size:12px;font-weight:700;text-align:center;line-height:45px}

/* articles */
.articles{position:absolute;left:150px;top:2932px;width:900px;height:131px;background:#e0e0e0}
.articles ul{list-style:none;position:absolute;left:18px;top:15px;font-size:13px;line-height:28px;color:#222}
.articles li::before{content:"• "}
.articles li.more{color:var(--teal);font-size:11px;line-height:26px}
.photo{position:absolute}

.site-footer{position:absolute;left:0;top:3118px;width:1200px;height:36px;background:var(--teal-deep);color:#fff;font-size:10px;font-weight:700}
.site-footer span{position:absolute;top:12px}
</style>
</head>
<body>

<header class="site-header">
  <div class="site-title">CLEAN ELECTRICITY</div>
  <div class="site-tagline">Global electricity data with a focus on low-carbon power sources</div>
</header>

<nav class="main-nav">
  <a class="active" href="#">Home</a><a href="#">Regions</a><a href="#">Power Sources</a><a href="#">Updates</a><a href="#">Resources</a>
</nav>
<div class="search"><span>Search Regions</span><b>SEARCH</b></div>
<div class="rule" style="top:134px"></div>

<h2 class="section-title" style="top:170px">Leading Regions In Development of Brisavolt Index</h2>

<!-- France -->
<div class="region-pill" style="top:231px">FRANCE</div>
<div class="progress-label" style="top:227px"><b>53.51% PROGRESS</b><small>1997-2018</small></div>
<div class="progress" style="top:231px"><div class="progress-fill" style="width:556px"><i>1997: 37.79%</i>2018: 91.3%</div></div>
<p class="region-text" style="top:278px">France Reduced the overall <em>Carbon Dioxide</em> Pollution by 2%, by just converting from oil to nuclear power. more than 380 <em>TWH</em> was generated from nuclear power. since 1979 [...]</p>
<div class="read-more" style="top:312px">READ MORE</div>

<!-- Denmark -->
<div class="region-pill hover" style="top:363px">DENMARK</div>
<div class="progress-label" style="top:359px"><b>60.65% PROGRESS</b><small>1990-2018</small></div>
<div class="progress" style="top:363px"><div class="progress-fill" style="width:390px"><i>1990: 3.18%</i>2018: 63.83%</div></div>
<p class="region-text" style="top:410px">Lorem ipsum dolor sit amet, consectetur adipisicing elit, sed do eiusmod tempor incididunt ut labore et dolore magna aliqua. Ut enim ad minim veniam, <em>quis laboris</em> nisi ut aliquip ex ea commodo consequat. Duis aute irure &nbsp;[...]</p>
<div class="read-more" style="top:441px">READ MORE</div>

<!-- Germany -->
<div class="region-pill" style="top:495px">GERMANY</div>
<div class="progress-label" style="top:491px"><b>34.72% PROGRESS</b><small>1990-2018</small></div>
<div class="progress" style="top:495px"><div class="progress-fill" style="width:257px"><i>1971: 6.86%</i>2018: 41.58%</div></div>
<p class="region-text" style="top:542px">Lorem ipsum dolor sit amet, consectetur adipisicing elit, sed do eiusmod tempor incididunt ut labore et dolore magna aliqua. Ut enim ad minim veniam, quis laboris nisi ut aliquip ex ea commodo consequat. Duis aute irure &nbsp;[...]</p>
<div class="read-more" style="top:572px">READ MORE</div>

<svg width="0" height="0" style="position:absolute">
  <defs>
    <linearGradient id="g-fossil" x1="0" y1="0" x2="0" y2="1"><stop offset="0" stop-color="#4c4c4c"/><stop offset="1" stop-color="#2a2a2a"/></linearGradient>
    <linearGradient id="g-fossil-hi" x1="0" y1="0" x2="0" y2="1"><stop offset="0" stop-color="#3d6b68"/><stop offset="1" stop-color="#28403f"/></linearGradient>
    <linearGradient id="g-clean" x1="0" y1="0" x2="0" y2="1"><stop offset="0" stop-color="#12bfc0"/><stop offset="1" stop-color="#3cdff5"/></linearGradient>
    <linearGradient id="g-clean-hi" x1="0" y1="0" x2="0" y2="1"><stop offset="0" stop-color="#3ff7f5"/><stop offset="1" stop-color="#2ee8f0"/></linearGradient>
    <linearGradient id="g-hydro" x1="0" y1="0" x2="0" y2="1"><stop offset="0" stop-color="#79a6fb"/><stop offset="1" stop-color="#5b8ff5"/></linearGradient>
    <linearGradient id="g-green" x1="0" y1="0" x2="0" y2="1"><stop offset="0" stop-color="#7ec83a"/><stop offset="1" stop-color="#5fb83a"/></linearGradient>
    <linearGradient id="g-sky" x1="0" y1="0" x2="0" y2="1"><stop offset="0" stop-color="#46e8f8"/><stop offset="1" stop-color="#2fd0ee"/></linearGradient>
    <g id="axis" font-family="Lato,sans-serif" font-size="8" fill="#444">
      <rect x="37" y="10" width="428" height="299" fill="#ececec"/>
      <line x1="37" y1="10" x2="37" y2="309" stroke="#777"/>
      <line x1="37" y1="309" x2="465" y2="309" stroke="#777"/>
      <text x="0" y="13">100%</text><text x="4" y="42">90%</text><text x="4" y="72">80%</text><text x="4" y="101">70%</text><text x="4" y="131">60%</text><text x="4" y="161">50%</text><text x="4" y="190">40%</text><text x="4" y="223">30%</text><text x="4" y="251">20%</text><text x="4" y="281">10%</text>
      <g text-anchor="middle"><text x="74.5" y="330">2009</text><text x="113.5" y="330">2010</text><text x="152.5" y="330">2011</text><text x="191.5" y="330">2012</text><text x="230.5" y="330">2013</text><text x="269.5" y="330">2014</text><text x="308.5" y="330">2015</text><text x="347.5" y="330">2016</text><text x="386.5" y="330">2017</text><text x="425.5" y="330">2018</text></g>
    </g>
  </defs>
</svg>

<!-- WORLD -->
<div class="data-label" style="top:668px">WORLD</div>
<div class="ctl" style="left:585px;top:665px;width:90px">2018</div>
<div class="ctl" style="left:690px;top:665px;width:120px">PERCENTAGE</div>
<div class="btn" style="left:825px;top:665px;width:120px">MORE DETAILS</div>
<div class="btn" style="left:960px;top:665px;width:90px">COMPARE</div>
<div class="rule" style="top:716px"></div>
<p class="summary" style="top:737px">35% of the electricity in World is generated from low-carbon power. The primary low-carbon power source is hydro.</p>

<svg class="abs" style="left:150px;top:805px" width="470" height="340" role="img" aria-label="World fossil and low-carbon share by year, 2009 to 2018">
  <use href="#axis"/>
  <g fill="url(#g-clean)">
    <rect x="59" y="10" width="31" height="32"/><rect x="98" y="10" width="31" height="41"/><rect x="137" y="10" width="31" height="56"/><rect x="176" y="10" width="31" height="71"/><rect x="215" y="10" width="31" height="80"/><rect x="254" y="10" width="31" height="86"/><rect x="293" y="10" width="31" height="86"/><rect x="332" y="10" width="31" height="86"/><rect x="371" y="10" width="31" height="98"/>
  </g>
  <rect x="410" y="10" width="31" height="104" fill="url(#g-clean-hi)"/>
  <g fill="url(#g-fossil)">
    <rect x="59" y="42" width="31" height="267"/><rect x="98" y="51" width="31" height="258"/><rect x="137" y="66" width="31" height="243"/><rect x="176" y="81" width="31" height="228"/><rect x="215" y="90" width="31" height="219"/><rect x="254" y="96" width="31" height="213"/><rect x="293" y="96" width="31" height="213"/><rect x="332" y="96" width="31" height="213"/><rect x="371" y="108" width="31" height="201"/>
  </g>
  <rect x="410" y="114" width="31" height="195" fill="url(#g-fossil-hi)"/>
  <rect x="37" y="321" width="14" height="14" fill="#222"/><path d="M46 324l-4 4 4 4" stroke="#fff" stroke-width="1.5" fill="none"/>
  <rect x="451" y="321" width="14" height="14" fill="#8a8a8a"/><path d="M456 324l4 4-4 4" stroke="#fff" stroke-width="1.5" fill="none"/>
</svg>

<svg class="abs" style="left:681px;top:790px" width="69" height="348" role="img" aria-label="World 2018 generation mix">
  <rect width="69" height="35" fill="url(#g-green)"/>
  <rect y="35" width="69" height="35" fill="url(#g-sky)"/>
  <rect y="70" width="69" height="55" fill="url(#g-hydro)"/>
  <rect y="125" width="69" height="223" fill="url(#g-fossil)"/>
</svg>
<p class="date" style="left:681px;top:1151px">Date: <em>2018</em></p>

<div class="info" style="top:815px">
  <p class="head">Nonfossil: 35.22%</p>
  <p class="key" style="--c:var(--hydro)">Hydro: 15.75%</p>
  <p class="key" style="--c:var(--nuclear)">Nuclear: 10.15%</p>
  <p class="key" style="--c:var(--renew)">Other Renewables: 9.32%</p>
  <p>Solar: 2.2%</p><p>Wind: 4.77%</p><p>Other: 2.35%</p>
  <p class="head sq gap" style="--c:#222">Fossil Fuel: 64.78%</p>
  <p>Coal: 36.18%</p><p>Oil: 1.72%</p><p>Gas: 19.39%</p><p>Unspecified: 6.91%</p>
  <div class="src"><span>Source: <em>KQ</em></span><span>Date: <em>2018</em></span></div>
</div>

<!-- MAP -->
<h2 class="section-title" style="top:1236px">Electricity generated from Low- Carbon Power Worldwide</h2>
<svg class="abs" style="left:0;top:1290px" width="1200" height="250" font-family="Lato,sans-serif">
  <defs><linearGradient id="g-map" x1="0" y1="0" x2="1" y2="1"><stop offset="0" stop-color="#e6e6e6"/><stop offset="1" stop-color="#d6d6d6"/></linearGradient></defs>
  <rect role="img" aria-label="Dotted world map" x="420" y="25" width="366" height="200" rx="14" fill="url(#g-map)"/>
  <polyline points="400,58 572,58 623,106" fill="none" stroke="#13b8e0" stroke-width="1.5"/>
  <polyline points="400,162 438,162 492,115" fill="none" stroke="#1b2d48" stroke-width="1.5"/>
  <polyline points="826,36 790,36 690,118" fill="none" stroke="#5fd6cf" stroke-width="1.5"/>
  <polyline points="786,170 740,170 604,149" fill="none" stroke="#f07a84" stroke-width="1.5"/>
  <circle cx="623" cy="106" r="7" fill="#13b8e0" stroke="#1b2d48" stroke-width="1.5"/>
  <circle cx="492" cy="115" r="8" fill="#1b2d48"/>
  <circle cx="690" cy="118" r="8" fill="#6fd9cf" stroke="#2d8f88" stroke-width="1.5"/>
  <circle cx="604" cy="149" r="7" fill="#f07a84" stroke="#c94a55" stroke-width="1"/>
  <g font-size="13" font-weight="700" fill="#fff" text-anchor="middle">
    <circle cx="370" cy="58" r="30" fill="#fff" stroke="#13b8e0" stroke-width="3"/><circle cx="370" cy="58" r="24" fill="#12bde3"/><text x="370" y="63" font-size="12">61.2%</text>
    <circle cx="370" cy="162" r="30" fill="#fff" stroke="#1b2d48" stroke-width="3"/><circle cx="370" cy="162" r="24" fill="#1b2d48"/><text x="370" y="167" font-size="12">37%</text>
    <circle cx="856" cy="36" r="30" fill="#fff" stroke="#7fe0d8" stroke-width="3"/><circle cx="856" cy="36" r="24" fill="#6fd6cd"/><text x="856" y="41" font-size="12">12.3%</text>
    <circle cx="816" cy="170" r="30" fill="#fff" stroke="#f5a3aa" stroke-width="3"/><circle cx="816" cy="170" r="24" fill="#f07a84"/><text x="816" y="175" font-size="12">2.7%</text>
  </g>
  <g font-size="12">
    <text x="278" y="62" fill="#3ab4d8">EUROPE</text>
    <text x="271" y="166" fill="#333">AMERICA</text>
    <text x="901" y="40" fill="#6fd0c8">ASIA</text>
    <text x="861" y="174" fill="#f07a84">AFRICA</text>
  </g>
</svg>

<!-- POWER SOURCES -->
<h2 class="section-title" style="top:1590px">Region Primary Power Source</h2>
<div class="source-pill" style="left:150px;background:linear-gradient(135deg,#5a4a3a,#2e2e2e)">NUCLEAR</div>
<div class="source-pill" style="left:283px;background:linear-gradient(135deg,#1c6fd0,#3aa0f0)">HYDRO</div>
<div class="source-pill" style="left:415px;background:linear-gradient(135deg,#2a2a2a,#4a4036)">SOLAR</div>
<div class="source-pill" style="left:548px;background:linear-gradient(135deg,#2e4a66,#5a5a5a)">WIND</div>
<div class="source-pill" style="left:681px;background:linear-gradient(135deg,#3a2a1c,#a0662a)">OIL</div>
<div class="source-pill" style="left:813px;background:linear-gradient(135deg,#1c1c1c,#3a3a3a)">COAL</div>
<div class="source-pill" style="left:946px;background:linear-gradient(135deg,#2c2c2c,#505050)">GAS</div>

<!-- NEPAL -->
<div class="data-label" style="top:1775px">NEPAL</div>
<div class="ctl" style="left:585px;top:1772px;width:90px">2018</div>
<div class="ctl" style="left:690px;top:1772px;width:120px">PERCENTAGE</div>
<div class="btn" style="left:825px;top:1772px;width:120px">MORE DETAILS</div>
<div class="btn" style="left:960px;top:1772px;width:90px">COMPARE</div>
<div class="rule" style="top:1823px"></div>
<p class="summary" style="top:1844px">100% of the electricity in Nepal is generated from <em>Low-Carbon Power</em>. The primary low-carbon power source is hydro.</p>

<svg class="abs" style="left:150px;top:1912px" width="470" height="340" role="img" aria-label="Nepal fossil and low-carbon share by year, 2009 to 2018">
  <use href="#axis"/>
  <g fill="url(#g-clean)">
    <rect x="59" y="10" width="31" height="299"/><rect x="98" y="10" width="31" height="299"/><rect x="137" y="10" width="31" height="299"/><rect x="176" y="10" width="31" height="299"/><rect x="215" y="10" width="31" height="299"/><rect x="254" y="10" width="31" height="299"/><rect x="293" y="10" width="31" height="299"/><rect x="332" y="10" width="31" height="299"/><rect x="371" y="10" width="31" height="299"/><rect x="410" y="10" width="31" height="299"/>
  </g>
  <g fill="url(#g-fossil)">
    <rect x="59" y="276" width="31" height="33"/><rect x="98" y="282" width="31" height="27"/><rect x="137" y="289" width="31" height="20"/><rect x="176" y="289" width="31" height="20"/><rect x="215" y="295" width="31" height="14"/>
  </g>
  <rect x="37" y="321" width="14" height="14" fill="#222"/><path d="M46 324l-4 4 4 4" stroke="#fff" stroke-width="1.5" fill="none"/>
  <rect x="451" y="321" width="14" height="14" fill="#8a8a8a"/><path d="M456 324l4 4-4 4" stroke="#fff" stroke-width="1.5" fill="none"/>
</svg>

<svg class="abs" style="left:681px;top:1897px" width="69" height="348" role="img" aria-label="Nepal 2018 generation mix">
  <rect width="69" height="348" fill="url(#g-hydro)"/>
</svg>
<p class="date" style="left:681px;top:2258px">Date: <em>2018</em></p>

<div class="info" style="top:1922px">
  <p class="head">Nonfossil: 100%</p>
  <p class="key" style="--c:var(--hydro)">Hydro: 100%</p>
  <p class="key" style="--c:var(--nuclear)">Nuclear: 0%</p>
  <p class="key" style="--c:var(--renew)">Other Renewables: 0%</p>
  <p>Solar: 0%</p><p>Wind: 0%</p><p>Other: 0%</p>
  <p class="head sq gap" style="--c:#222">Fossil Fuel: 0%</p>
  <p>Coal: 0%</p><p>Oil: 0%</p><p>Gas: 0%</p><p>Unspecified: 0%</p>
  <div class="src"><span>Source: <em>KQ</em></span><span>Date: <em>2018</em></span></div>
</div>

<!-- ICELAND -->
<div class="data-label" style="top:2313px">ICELAND</div>
<div class="ctl" style="left:585px;top:2310px;width:90px">2018</div>
<div class="ctl" style="left:690px;top:2310px;width:120px">PERCENTAGE</div>
<div class="btn" style="left:825px;top:2310px;width:120px">MORE DETAILS</div>
<div class="btn" style="left:960px;top:2310px;width:90px">COMPARE</div>
<div class="rule" style="top:2361px"></div>
<p class="summary" style="top:2382px">100% of the electricity in Iceland is generated from <em>Low-Carbon Power</em>. The primary low-carbon power source is hydro.</p>

<svg class="abs" style="left:150px;top:2450px" width="470" height="340" role="img" aria-label="Iceland fossil and low-carbon share by year, 2009 to 2018">
  <use href="#axis"/>
  <g fill="url(#g-clean)">
    <rect x="59" y="10" width="31" height="299"/><rect x="98" y="10" width="31" height="299"/><rect x="137" y="10" width="31" height="299"/><rect x="176" y="10" width="31" height="299"/><rect x="215" y="10" width="31" height="299"/><rect x="254" y="10" width="31" height="299"/><rect x="293" y="10" width="31" height="299"/><rect x="332" y="10" width="31" height="299"/><rect x="371" y="10" width="31" height="299"/><rect x="410" y="10" width="31" height="299"/>
  </g>
  <g fill="#222">
    <rect x="59" y="306" width="31" height="3"/><rect x="98" y="306" width="31" height="3"/><rect x="137" y="306" width="31" height="3"/><rect x="176" y="306" width="31" height="3"/><rect x="215" y="306" width="31" height="3"/>
  </g>
  <rect x="37" y="321" width="14" height="14" fill="#222"/><path d="M46 324l-4 4 4 4" stroke="#fff" stroke-width="1.5" fill="none"/>
  <rect x="451" y="321" width="14" height="14" fill="#222"/><path d="M456 324l4 4-4 4" stroke="#fff" stroke-width="1.5" fill="none"/>
</svg>

<svg class="abs" style="left:681px;top:2435px" width="69" height="348" role="img" aria-label="Iceland 2018 generation mix">
  <rect width="69" height="105" fill="url(#g-green)"/>
  <rect y="105" width="69" height="243" fill="url(#g-hydro)"/>
</svg>
<p class="date" style="left:681px;top:2796px">Date: <em>2018</em></p>

<div class="info" style="top:2460px">
  <p class="head">Nonfossil: 99.8%</p>
  <p class="key" style="--c:var(--hydro)">Hydro: 69.53%</p>
  <p class="key" style="--c:var(--nuclear)">Nuclear: NA</p>
  <p class="key" style="--c:var(--renew)">Other Renewables: 30.27%</p>
  <p>Solar: 0%</p><p>Wind: 0.02%</p><p>Other: 30.25%</p>
  <p class="head sq gap" style="--c:#222">Fossil Fuel: 0.2%</p>
  <p>Coal: 0%</p><p>Oil: 0%</p><p>Gas: 0%</p><p>Unspecified: 0.2%</p>
  <div class="src"><span>Source: <em>KQ</em></span><span>Date: <em>2018</em></span></div>
</div>

<!-- ARTICLES -->
<h2 class="section-title" style="top:2826px;font-size:18px">More Articles &amp; Links</h2>
<div class="articles">
  <ul>
    <li>What countries use the most Low-Carbon Power for electricity generation?</li>
    <li>What is the Primary Low-Carbon Power in Europe?</li>
    <li>What are the Advantages of Low-Carbon Powers over fuel based generators?</li>
    <li class="more">Find More Articles</li>
  </ul>
</div>
<div class="photo" role="img" aria-label="Photo of a dam spillway with water" style="left:852px;top:2876px;width:185px;height:187px;background:linear-gradient(135deg,#3a4a48,#6a7a76 45%,#b8b4ac)"></div>
<div class="photo" role="img" aria-label="Photo of cooling towers at sunset" style="left:755px;top:2930px;width:150px;height:148px;background:linear-gradient(180deg,#4a5a7a,#a07a8a 55%,#d89a6a 80%,#3a3040)"></div>

<footer class="site-footer">
  <span style="left:150px">Copyright © Clean Electricity 2020</span>
  <span style="right:150px">FAQ | Privacy</span>
</footer>

</body>
</html>
```